KORBALT

The business want a professional looking business card. We have a scetch we will add but want the extra upgrade, and would like more suggestions for variations of our business cards.

```html
<!DOCTYPE html>
<html lang="en">
<head>
<meta charset="utf-8">
<title>KORBALT – Business Card</title>
<link rel="stylesheet" href="https://fonts.googleapis.com/css2?family=Cinzel:wght@400;700&family=Quicksand:wght@400;500&display=swap">
<style>
  :root {
    --bg: #e4e4e4;
    --card: #201e1f;
    --gold: #d6ac3c;
    --gold-soft: #c99c35;
    --pattern-light: #4a4849;
    --pattern-dark: #2a2829;
  }
  * { margin: 0; padding: 0; box-sizing: border-box; }
  html, body { width: 1200px; height: 745px; overflow: hidden; }
  body {
    background: var(--bg);
    display: flex;
    align-items: center;
    justify-content: center;
    gap: 40px;
    font-family: "Quicksand", sans-serif;
  }
  .card {
    position: relative;
    width: 560px;
    height: 320px;
    background: var(--card);
    box-shadow: 0 12px 30px rgba(0,0,0,.18);
    color: var(--gold);
  }
  /* front */
  .brand-block {
    position: absolute;
    left: 40px; top: 0; width: 210px; height: 100%;
    display: flex; flex-direction: column; align-items: center; justify-content: center;
  }
  .brand-mark {
    width: 22px; height: 22px; border-radius: 50%;
    background: var(--gold); margin-bottom: 18px;
  }
  .brand-name {
    font-family: "Cinzel", serif; font-weight: 400;
    font-size: 22px; letter-spacing: 9px; padding-left: 9px;
  }
  .brand-since {
    font-size: 8px; letter-spacing: 1.5px; margin-top: 6px;
  }
  .divider {
    position: absolute; left: 272px; top: 50px;
    width: 1px; height: 220px; background: var(--gold-soft);
  }
  .details {
    position: absolute; left: 300px; top: 88px;
  }
  .company-title {
    font-family: "Cinzel", serif; font-weight: 700;
    font-size: 19px; letter-spacing: .5px; line-height: 1.1;
  }
  .person-name { font-size: 11.5px; font-weight: 500; margin-top: 3px; }
  .person-role { font-size: 10px; margin-top: 2px; }
  .contact-list { list-style: none; margin-top: 14px; }
  .contact-list li {
    display: flex; align-items: center; gap: 10px;
    font-size: 12.5px; line-height: 22px;
  }
  .contact-list svg { width: 11px; height: 11px; flex: none; }
  /* back */
  .pattern-field {
    position: absolute; inset: 0;
    background: radial-gradient(circle at 40% 60%, var(--pattern-light) 0%, var(--pattern-dark) 70%);
    opacity: .55;
  }
  .back-brand {
    position: absolute; top: 22px; right: 26px;
    font-family: "Cinzel", serif; font-weight: 400;
    font-size: 13px; letter-spacing: 3px;
  }
</style>
</head>
<body>
  <section class="card card-front">
    <div class="brand-block">
      <span class="brand-mark"></span>
      <div class="brand-name">KORBALT</div>
      <div class="brand-since">SINCE 2026</div>
    </div>
    <div class="divider"></div>
    <div class="details">
      <h1 class="company-title">KORBALT MOBERG</h1>
      <p class="person-name">LARS ERIK MOBERG</p>
      <p class="person-role">ceo &amp; founder</p>
      <ul class="contact-list">
        <li>
          <svg viewBox="0 0 12 12" fill="none" stroke="currentColor" stroke-width="1"><path d="M3 1.5l1.5 2.5-1 1c.6 1.3 1.5 2.2 2.5 2.8l1-1 2.5 1.5-.8 1.7C5.5 9.8 2.2 6.5 1.3 2.3z"/></svg>
          <span>004791234567</span>
        </li>
        <li>
          <svg viewBox="0 0 12 12" fill="none" stroke="currentColor" stroke-width="1"><rect x="1" y="2.5" width="10" height="7"/><path d="M1 2.5l5 4 5-4"/></svg>
          <span>korbalt.llc@postmail.com</span>
        </li>
        <li>
          <svg viewBox="0 0 12 12" fill="none" stroke="currentColor" stroke-width="1"><path d="M2 1l7 4-3 1 2 4-1 .6-2-4-2.5 2z"/></svg>
          <span>www.korbalt.llc</span>
        </li>
      </ul>
    </div>
  </section>

  <section class="card card-back">
    <div class="pattern-field" role="img" aria-label="Repeating grey brand pattern covering the card back"></div>
    <div class="back-brand">KORBALT</div>
  </section>
</body>
</html>
```